Restaurant Menu - redesign.

to create a younger more visual menu .
Introduce a trendy more current look and easier to navigate.
Appealing to a more sophisticated customer. look at current
See Web site for current menu. Restaurant is known for its Build your own Ridgecrest Burger. & A Large Salad Bar.
www.thepelfhouse.com
Target Market(s)
16yr. to 60 yr.- Family Restaurant located in upscale mall.
Industry/Entity Type
Restaurant

```html
<!DOCTYPE html>
<html lang="en">
<head>
<meta charset="utf-8">
<title>Grub Stake Starters – Pelf House</title>
<link href="https://fonts.googleapis.com/css2?family=Anton&family=Montserrat:ital,wght@0,400;0,600;0,700;0,800;1,400&display=swap" rel="stylesheet">
<style>
  :root {
    --paper: #f7f7f7;
    --paper-edge: #d9d9d9;
    --ink: #111111;
    --body: #2a2a2a;
    --red: #d7192a;
    --rule: #555555;
  }
  * { margin: 0; padding: 0; box-sizing: border-box; }
  html, body { width: 1000px; height: 1200px; overflow: hidden; }
  body {
    position: relative;
    background:
      radial-gradient(ellipse 70% 60% at 45% 45%, #ffffff 0%, var(--paper) 55%, var(--paper-edge) 100%);
    font-family: "Montserrat", Arial, sans-serif;
    color: var(--body);
  }
  .menu-title {
    position: absolute; left: 142px; top: 96px;
    font-family: "Anton", Impact, sans-serif; font-weight: 400;
    font-size: 72px; line-height: 68px; letter-spacing: -0.5px;
    color: var(--ink); text-transform: uppercase;
  }
  .item { position: absolute; width: 335px; }
  .item-name {
    font-weight: 800; font-size: 17px; color: var(--red);
    text-transform: uppercase; letter-spacing: 0.2px; line-height: 22px;
    white-space: nowrap; position: relative;
  }
  .price { color: var(--ink); font-weight: 700; }
  .sep { color: var(--rule); font-weight: 400; margin: 0 5px; }
  .item-desc { font-size: 12.2px; line-height: 15.3px; margin-top: 4px; }
  .item-desc em { font-style: italic; }
  .addon { color: var(--red); font-weight: 700; }
  .opt { font-weight: 700; color: var(--ink); }
  .sub { margin-top: 3px; font-size: 12.2px; line-height: 15.3px; }
  .sig-mark {
    position: absolute; left: -22px; top: 6px; width: 10px; height: 10px;
    border-radius: 50%; background: var(--ink);
  }
  .chili { display: inline-block; width: 28px; height: 14px; vertical-align: middle; margin-left: 6px; }
  .legend { position: absolute; left: 115px; font-size: 11px; color: var(--body); display: flex; align-items: center; gap: 8px; }
  .legend .legend-dot { width: 10px; height: 10px; border-radius: 50%; background: var(--ink); margin: 0 6px; }
  .legend svg { width: 22px; height: 16px; }
  .brand-name {
    position: absolute; left: 0; right: 0; top: 1108px; text-align: center;
    font-family: "Montserrat", Arial, sans-serif; font-weight: 800; font-size: 15px;
    color: var(--ink); text-transform: uppercase; letter-spacing: 0.5px;
  }
</style>
</head>
<body>

<svg width="0" height="0" style="position:absolute">
  <defs>
    <symbol id="chili" viewBox="0 0 28 14">
      <path d="M2 4 Q10 12 24 8 Q26 7 24 5 Q14 7 6 3 Z" fill="#d7192a"/>
      <path d="M23 6 Q25 2 27 3" stroke="#2d7a2d" stroke-width="1.6" fill="none" stroke-linecap="round"/>
    </symbol>
  </defs>
</svg>

<h1 class="menu-title">Grub Stake<br>Starters</h1>

<!-- Left column -->
<section class="item" style="left:142px; top:253px;">
  <span class="sig-mark"></span>
  <h2 class="item-name">Steamed Whole Artichoke<span class="sep">|</span><span class="price">8.29</span></h2>
  <p class="item-desc">Served with a side of drawn butter and lemonaise. A Pelf House Creation. Perfect for sharing! <em>(Subject to seasonal availability; at times this favorite is temporarily unavailable. It’s worth coming back for!)</em></p>
</section>

<section class="item" style="left:142px; top:360px;">
  <span class="sig-mark"></span>
  <h2 class="item-name">Chipotle Chicken Wings<span class="sep">|</span><span class="price">10.49</span><svg class="chili"><use href="#chili"/></svg></h2>
  <p class="item-desc">Marinated in our own special chipotle and herb rub, baked, then flash fried and tossed in hot sauce. Served with ranch dressing.</p>
  <p class="sub"><span class="addon">Boneless</span> <em>(Buffalo, Plain, or BBQ)</em><span class="sep">|</span><span class="opt">8.49</span></p>
</section>

<section class="item" style="left:142px; top:470px;">
  <span class="sig-mark"></span>
  <h2 class="item-name">Baked French Onion Soup<span class="sep">|</span><span class="price">5.50</span></h2>
  <p class="item-desc">Our take on this smooth and savory classic is topped with melted provolone and Parmesan cheeses. Served with garlic toast.</p>
</section>

<section class="item" style="left:142px; top:562px;">
  <span class="sig-mark"></span>
  <h2 class="item-name">Chicken Cajun Egg Rolls<span class="sep">|</span><span class="price">8.99</span><svg class="chili"><use href="#chili"/></svg></h2>
  <p class="item-desc">Four woton wraps filled with mozzarella cheese and blackened chicken. Served with a honey Dijon dipping sauce.</p>
</section>

<section class="item" style="left:142px; top:652px;">
  <h2 class="item-name">Guacamole Nachos<span class="sep">|</span><span class="price">8.49</span></h2>
  <p class="item-desc">A mountain of fresh tortilla chips loaded with melted cheddar. Served with sides of guacamole, sour cream, salsa, and vegetarian refried beans. Garnished with scallions.<br>
  <span class="addon">Add taco meat</span><span class="sep">|</span>2.99<br>
  <span class="addon">Add diced chicken</span><span class="sep">|</span>2.50<br>
  <span class="addon">Add turkey chili</span><span class="sep">|</span>2.99</p>
</section>

<section class="item" style="left:142px; top:808px;">
  <h2 class="item-name">Fried Green Beans Basket<span class="sep">|</span><span class="price">8.99</span></h2>
  <h2 class="item-name">Beer Batter Onion Rings<span class="sep">|</span><span class="price">8.99</span></h2>
  <p class="item-desc">Fried green beans or beer battered onion rings coated in a crunch golden brown crust, and served with BBQ ranch dipping sauce and house sauce.</p>
</section>

<section class="item" style="left:142px; top:930px;">
  <h2 class="item-name" style="font-size:15.5px">Creamy Spinach &amp; Artichoke Dip<span class="sep">|</span><span class="price">9.99</span></h2>
  <p class="item-desc">Spinach, artichoke hearts and four cheeses served hot with baked flour tortilla chips.</p>
</section>

<p class="legend" style="top:1019px;"><span class="legend-dot"></span>Pelf House Signature Item</p>
<p class="legend" style="top:1042px;"><svg><use href="#chili"/></svg>Spicy Item</p>

<!-- Right column -->
<section class="item" style="left:537px; top:103px;">
  <h2 class="item-name">Flatbread Pizza<span class="sep">|</span><span class="price">10.49</span></h2>
  <p class="item-desc"><span class="addon">BBQ Chicken</span><span class="sep">|</span>BBQ sauce, chicken, cheddar and Monterey Jack cheeses, shaved red onion and scallions.</p>
  <p class="item-desc"><span class="addon">Southwestern Chicken</span><span class="sep">|</span>Salsa, chicken, cheddar and Monterey Jack cheeses, tomato, scallions and guacamole.</p>
</section>

<section class="item" style="left:537px; top:243px;">
  <h2 class="item-name">Mozzarella Marinara Sticks<span class="sep">|</span><span class="price">7.95</span></h2>
  <p class="item-desc">Dig into five hand-rolled wonton wrappers stuffed with melted mozzarella cheese and served with a side of marinara sauce.</p>
</section>

<section class="item" style="left:537px; top:334px;">
  <h2 class="item-name">Blackened Ahi Tuna<span class="sep">|</span><span class="price">10.99</span><svg class="chili"><use href="#chili"/></svg></h2>
  <p class="item-desc">Thin slices of blackened Ahi tuna served over chilled soba noodles with carrots, scallions, and red peppers tossed in a Thai peanut sauce. Accompanied by a soy wasabi diping sauce.</p>
</section>

<section class="item" style="left:537px; top:438px;">
  <h2 class="item-name">BBQ Chicken Quesadilla<span class="sep">|</span><span class="price">10.99</span></h2>
  <p class="item-desc">A jumbo flour tortilla stuffed and grilled with BBQ chicken, Monterey Jack cheese, and fried onions. Served with guacamole, sour cream, and salsa.</p>
</section>

<section class="item" style="left:537px; top:533px;">
  <h2 class="item-name">Cheese Quesadilla<span class="sep">|</span><span class="price">6.99</span></h2>
  <p class="item-desc">A jumbo flour tortilla stuffed with Monterey Jack cheese and scallions. Served with guacamole, sour cream, and salsa. <em>Add chicken</em><span class="sep">|</span>2.50</p>
</section>

<section class="item" style="left:537px; top:625px;">
  <h2 class="item-name">Gold Rush Potato Skins<span class="sep">|</span><span class="price">8.29</span></h2>
  <p class="item-desc">Idaho potato skins filled with melted cheddar cheese, bacon, and scallions. Served with sour cream.</p>
</section>

<section class="item" style="left:537px; top:700px;">
  <h2 class="item-name">PH Mini Sliders</h2>
  <p class="item-desc"><span class="opt">Spicy Buffalo Chicken</span><span class="sep">|</span>Topped with crumbled bleu cheese.<span class="sep">|</span><span class="opt">8.25</span></p>
  <p class="sub"><span class="opt">Pulled BBQ Chicken</span><span class="sep">|</span><span class="opt">8.50</span></p>
  <p class="sub"><span class="opt">Mini Burgers</span><span class="sep">|</span>With American cheese, sautéed onions &amp; mushrooms and fried onions.<span class="sep">|</span><span class="opt">8.99</span></p>
</section>

<section class="item" style="left:537px; top:827px;">
  <h2 class="item-name">Loaded Pelf Chip Basket<span class="sep">|</span><span class="price">6.99</span></h2>
  <p class="item-desc">Covered with Halvor’s Wisconsin Cheese<br>
  <em>Add Spicy Ground Beef</em><span class="sep">|</span>7.99<svg class="chili"><use href="#chili"/></svg><br>
  <em>Add Turkey Chili</em><span class="sep">|</span>8.99</p>
</section>

<section class="item" style="left:537px; top:924px;">
  <h2 class="item-name">Turkey Chili</h2>
  <p class="item-desc">Bowl<span class="sep">|</span><span class="opt">5.99</span>&nbsp;&nbsp;&nbsp; Cup<span class="sep">|</span><span class="opt">4.99</span></p>
</section>

<section class="item" style="left:537px; top:987px;">
  <h2 class="item-name">Soup of the Day</h2>
  <p class="item-desc">Bowl<span class="sep">|</span><span class="opt">4.99</span>&nbsp;&nbsp;&nbsp; Cup<span class="sep">|</span><span class="opt">3.99</span></p>
</section>

<p class="brand-name">Pelf House</p>

</body>
</html>
```